Concrete Grinding and Polishing company business card with logo, based in Australia.

We need a business card design along with logo for a new company based in Melbourne called HexaSheen. We specialise in the grinding and polishing of concrete. Polished concrete is durable, easy to maintain, cost effective, dust proof, has increased light reflectivity, and is slip resistant, among other benefits. In short, polished concrete is a popular flooring solution because of its practical advantages, as well as it's decorative appeal.

Industry/Entity Type

Business

Requirements
Must have
• It must have the company name(HexaSheen) as well as the slogan: A Cut Above The Rest.
Nice to have
• Something that symbolises polished concrete. Would also like it to have a silver background with black writing, if possible.

```html
<!DOCTYPE html>
<html lang="en">
<head>
<meta charset="utf-8">
<title>HexaSheen Business Card</title>
<link rel="stylesheet" href="https://fonts.googleapis.com/css2?family=Economica:wght@400;700&display=swap">
<style>
  :root {
    --stage: #000000;
    --ink: #111114;
    --rule: #2a2a2e;
    --silver-dark: #a9aaaf;
    --silver-mid: #c6c7cc;
    --silver-light: #e8ebf1;
    --silver-sheen: #f3f5fa;
  }
  html, body {
    margin: 0;
    padding: 0;
    width: 1200px;
    height: 900px;
    overflow: hidden;
    background: var(--stage);
  }
  .canvas {
    position: relative;
    width: 1200px;
    height: 900px;
    background: var(--stage);
  }
  .business-card {
    position: absolute;
    left: 200px;
    top: 206px;
    width: 780px;
    height: 496px;
    border-radius: 16px;
    overflow: hidden;
    background:
      linear-gradient(100deg,
        var(--silver-dark) 0%,
        var(--silver-mid) 22%,
        var(--silver-light) 48%,
        var(--silver-sheen) 56%,
        var(--silver-mid) 74%,
        var(--silver-light) 90%,
        var(--silver-mid) 100%);
    font-family: "Economica", "Arial Narrow", sans-serif;
    color: var(--ink);
  }
  .brushed-finish {
    position: absolute;
    inset: 0;
    background: repeating-linear-gradient(0deg,
      rgba(255,255,255,0.05) 0px,
      rgba(255,255,255,0.05) 1px,
      rgba(0,0,0,0.025) 2px,
      rgba(0,0,0,0.025) 3px);
  }
  .company-name {
    position: absolute;
    left: 66px;
    top: 82px;
    margin: 0;
    font-size: 66px;
    font-weight: 400;
    letter-spacing: 5px;
    line-height: 1;
  }
  .name-rule {
    position: absolute;
    left: 60px;
    top: 162px;
    width: 662px;
    height: 2px;
    background: var(--rule);
  }
  .slogan {
    position: absolute;
    left: 68px;
    top: 176px;
    margin: 0;
    font-size: 31px;
    font-weight: 700;
    letter-spacing: 5px;
    line-height: 1;
  }
  .contact-details {
    position: absolute;
    right: 54px;
    top: 344px;
    margin: 0;
    text-align: right;
    font-style: normal;
    font-size: 26px;
    font-weight: 400;
    letter-spacing: 4px;
    line-height: 34px;
  }
</style>
</head>
<body>
<main class="canvas">
  <section class="business-card" aria-label="HexaSheen business card">
    <div class="brushed-finish"></div>
    <h1 class="company-name">HexaSheen</h1>
    <div class="name-rule"></div>
    <p class="slogan">A Cut Above The Rest</p>
    <address class="contact-details">
      Your Office Address<br>
      www.hexasheen.com.au<br>
      (03)555-0142
    </address>
  </section>
</main>
</body>
</html>
```